Dune Circle UAE - Website for Club Members

Dune Circle UAE Website

A simple but amazing website is needed for an offroad club in the UAE.

Dunecircle.ae (domain owned)
Hosting required.

Dune Circle UAE is a non-profit club that brings together Kovo owners who meet up and drive & gather together all over the country.

The club until now has been working on WhatsApp but has grown to over 700+ members and needs a website to support it and have a platform to book/sign up for trips. As there are many types of driving levels, we need a platform to categorise each member according to their driving skill so they can only signup for the trip that is in accordance with their level.

The page must be intuitive, easy and clean. We have many members from many different countries & ages. Keeping it simple would be good.
English is the main language. (Maybe an easy Google translation addon for Arabic)

Mobile friendly / web app:
Most of our members will use the page on their mobile, and admins will usually use the site on their mobiles to see who is on the trip, show reports, blog etc.

1. Member profile creation
● Login
● Sign up
● Recover password
• (Terms & Conditions Button) Captcha

2. Member Area
● Dynamic ranking (Admins to set levels)
• Master Admin (Master Access)
• Admins (Full Access)
• Management (Edit Options)
• Marshalls (Can Post Trips & add post-trip report)

● Member Level
• Trail (Beginner)
• Mesa (Intermediate)
• Falcon (Advanced)
• Warden (Expert)
• 517 (Teacher)
● Profile (Vehicle & Member info)

3. Member trip/events sign-ups
• Members can only see trips according to their tier
• (Example) Only Trail Should see Trips for “Trail Level” / Mesa can see Mesa Trips & Trail Trips / Falcon can see Falcon, Mesa & Trail Trips etc. Tiers can only see their level and below.
● A page with the list of trips (group by date)
● Sign up/out button
● The trip will contain:
○ Title
○ Picture
○ Description
○ Time and Location
○ Level limit
○ Trip creator/owner
○ Trip capacity limit
● Admin: add/remove members from trip
● Admin can create/manage trips
● Admin can rate (1 rating 1 to 5 stars) members in the trip

4. Sponsors Pages/s (tesk4x4, vol)
• Ability to add full pages according to the sponsorship level.
• Speciality Index (Fabrication, Mechanic, Wheel, Rims, painting)
● Ad area with Title, image, a short description and link

5. Dune Circle profile
• About Us page
• Rules and regulations, T&C’s.
• Roles
• Founders/Management area.

6, Blog Area.
• General blog, nothing complicated
• For example, an area where members can sell their used items, an area where they can chit-chat about new models etc.
• Only Admins can create posts/subjects.
• Blogs post should also be seen as per Member Level

7, Social media area.
● Simple place where we share our social media. @dunecircle.ae
• We only use Social channel (plain circle) for now but we will push Tik Tok soon.

8, E-Commerce
• Not a must at this moment but will be required in the future (1 year). Please account for this so we can activate it when required. Simple and easy.

9, Backend

• Backend Should be straightforward to use and intuitive, adding images/text, editing images/text, creating text (Font, size, colour), and adding pages. (For simple people to use one site). We do not require website management, but we will contact the developer if we need any big add-ons or want to expand the site.
• Mobile view is essential.
o We will use the website as a Web App for mobile devices. Mobile versions should be accessible, mobile like and intuitive.
• Apple Wallet / Google Wallet Membership Card option required. Members will be able to download their membership cards. (Simple, no picture) members details

Website References:
Dunecircle.ae (old website)
QP4x4
Lumen 4x4
UAE Trailhounds
Bravely 4x4

Target Market(s)

Club members & future club members

Industry/Entity Type

Offroad club

Coding

Coded - Design and coding required

Number of Pages Required

5+ page

Font styles to use
Other font styles liked:
• Helvetica

Colors
0054AA
0677BA
7BADD7
CADEEF
E8F1F8
EB3D1F
EC4F4E
F09395
F8D3D4
FCEDEE

Requirements
Must have
• Member/Profile Area, Member Level, Trips/Events area, Sponsors, Profile, Blog, E-commerce, easy & intuative backend.
Nice to have
• Simple, clean, attaractive, modern. Apple Wallet & Google Wallet option for memebers to downalod their mebership cards.
Should not have
• A very complicated backend.

```html
<!DOCTYPE html>
<html lang="en">
<head>
<meta charset="utf-8">
<title>Dune Circle UAE</title>
<link rel="stylesheet" href="https://fonts.googleapis.com/css2?family=Poppins:wght@400;500;600;700&display=swap">
<style>
:root{
  --blue:#0c3a9c;
  --blue-dark:#082a78;
  --ink:#050a14;
  --text:#111111;
  --muted:#555b66;
  --red:#e11f26;
  --white:#ffffff;
  --line:#c9ccd2;
  --star:#f5b800;
  --sand:#c98a4e;
}
*{box-sizing:border-box;margin:0;padding:0}
html,body{width:1200px;height:4468px;overflow:hidden}
body{position:relative;background:var(--white);font-family:"Poppins",Helvetica,Arial,sans-serif;color:var(--text)}
.abs{position:absolute}

/* nav */
.site-nav{position:absolute;left:0;top:0;width:1200px;height:88px;background:var(--white);border-bottom:1px solid #e6e6e6}
.brand{position:absolute;left:113px;top:28px;display:flex;align-items:center;gap:8px;font-weight:700;font-size:19px;color:var(--red)}
.brand-mark{width:14px;height:14px;background:var(--red)}
.nav-links{position:absolute;top:36px;left:0;font-size:15px}
.nav-links a{position:absolute;white-space:nowrap;color:var(--text);text-decoration:none}
.sign-up{position:absolute;left:976px;top:28px;width:108px;height:36px;border:1.5px solid #333;display:flex;align-items:center;justify-content:center;gap:6px;font-size:15px}

/* hero */
.hero{position:absolute;left:0;top:88px;width:1200px;height:573px;background:linear-gradient(180deg,#3c5a7a 0%,#8c6a4e 45%,#b9814d 70%,#8a5630 100%)}
.hero-title{position:absolute;left:0;width:1200px;text-align:center;color:var(--white);font-weight:700;font-size:86px;line-height:1}
.btn-light{position:absolute;left:510px;top:385px;width:180px;height:58px;background:var(--white);border-radius:8px;display:flex;align-items:center;justify-content:center;font-weight:600;font-size:20px}

/* section titles */
.section-title{position:absolute;left:0;width:1200px;text-align:center;font-weight:600;font-size:35px}

/* split buttons */
.split-btn{position:absolute;background:var(--white);border-radius:6px;box-shadow:0 4px 12px rgba(0,0,0,.18);overflow:hidden}
.split-btn .label{position:absolute;left:0;top:0;height:100%;background:var(--blue);clip-path:polygon(0 0,100% 0,78% 100%,0 100%);color:var(--white);font-weight:600;display:flex;align-items:center;padding-left:13px}
.split-btn.dark .label{background:var(--ink)}
.split-btn svg{position:absolute;top:50%;transform:translateY(-50%)}
.area-btn{width:222px;height:73px}
.area-btn .label{width:175px;font-size:18px}
.area-btn svg{right:16px;width:38px;height:38px}
.level-btn{width:182px;height:61px}
.level-btn .label{width:142px;font-size:15px}
.level-btn svg{right:14px;width:32px;height:32px}

/* events */
.events{position:absolute;left:0;top:1436px;width:1200px;height:607px;background:var(--ink)}
.event-card{position:absolute;top:73px;width:283px;height:461px;background:var(--white);border-radius:8px;overflow:hidden}
.event-card .photo{height:231px}
.event-card h3{text-align:center;font-weight:600;font-size:22px;margin-top:18px}
.event-card p{text-align:center;font-size:12px;line-height:18px;color:#333;margin:14px 30px 0}
.meta{position:absolute;left:14px;right:14px;font-size:11px;display:flex;align-items:center;gap:6px}
.meta span{display:flex;align-items:center;gap:4px}
.bar{position:absolute;left:120px;width:145px;height:9px;border-radius:5px;background:#c4c4c4;overflow:hidden}
.bar i{display:block;height:100%;border-radius:5px}
.events h2{position:absolute;left:780px;top:100px;color:var(--white);font-size:40px;font-weight:600}
.events .copy{position:absolute;left:787px;top:170px;width:280px;color:var(--white);font-size:15px;line-height:30px}

/* about */
.about-copy{position:absolute;left:230px;top:2186px;width:740px;text-align:center;font-size:15px;line-height:29px;color:#333}
.photo-block{position:absolute;border-radius:8px}

/* gallery arrows */
.arrow-nav{position:absolute;top:3054px;width:20px;height:20px}

/* blog */
.blog-card{position:absolute;background:var(--white);border-radius:14px;box-shadow:0 4px 16px rgba(0,0,0,.16);overflow:hidden}
.blog-card .photo{position:absolute;left:0;right:0;top:0;height:248px;border-radius:14px}
.blog-card.featured .photo{left:20px;right:20px;top:21px}
.blog-body{position:absolute;left:32px;font-size:16px}
.blog-body h4{font-weight:600;font-size:16px;line-height:30px}
.stars{color:var(--star);font-size:15px;letter-spacing:1px;margin-top:14px}
.blog-body small{display:block;font-size:11px;margin-top:8px}

/* sponsors & footer */
.footer{position:absolute;left:0;top:4054px;width:1200px;height:414px;background:var(--ink);color:var(--white)}
.sponsors{position:absolute;left:111px;top:3978px;width:978px;height:160px;background:var(--white);box-shadow:0 4px 14px rgba(0,0,0,.12);display:flex;align-items:center;justify-content:space-around;padding:0 20px}
.sponsor{display:flex;align-items:center;gap:8px;font-weight:600;font-size:20px;letter-spacing:1px;color:#222}
.sponsor i{width:30px;height:30px;border-radius:50%;background:#d6d9de}
.pay-row{position:absolute;left:111px;top:4145px;display:flex;align-items:center;gap:24px;font-size:32px;font-weight:500}
.social-dot{width:32px;height:32px;border-radius:50%;background:var(--white)}
.foot-links{position:absolute;left:111px;top:4272px;font-size:16px;display:flex;gap:18px}
.foot-links b{font-weight:400}
.legal{position:absolute;left:111px;top:4315px;font-size:12px}
.foot-note{position:absolute;left:111px;top:4347px;width:620px;font-size:12px;line-height:22px}
.foot-brand{position:absolute;left:890px;top:4203px;width:197px;height:198px;background:var(--white);display:flex;align-items:center;justify-content:center;gap:8px;color:var(--red);font-weight:700;font-size:24px}
</style>
</head>
<body>

<header class="site-nav">
  <div class="brand"><span class="brand-mark"></span>Dune Circle</div>
  <nav class="nav-links">
    <a style="left:309px">Home</a>
    <a style="left:395px">The Club</a>
    <a style="left:505px">Community</a>
    <a style="left:636px">Forums</a>
    <a style="left:735px">Trips</a>
    <a style="left:813px">Blog</a>
    <a style="left:876px;display:flex;align-items:center;gap:6px">
      <svg width="16" height="16" viewBox="0 0 16 16"><path d="M5 3.5a6 6 0 1 0 6 0" fill="none" stroke="#e11f26" stroke-width="2"/><path d="M8 1v7" stroke="#e11f26" stroke-width="2"/></svg>Log In</a>
  </nav>
  <div class="sign-up">
    <svg width="16" height="16" viewBox="0 0 16 16"><circle cx="7" cy="5" r="3.5" fill="#e11f26"/><path d="M1 15c0-4 3-6 6-6s6 2 6 6z" fill="#e11f26"/></svg>Sign Up
  </div>
</header>

<section class="hero" role="img" aria-label="Photo of a club leader with arms spread in the desert, a line of off-road vehicles on the dunes behind him">
  <div class="hero-title" style="top:126px">Welcome</div>
  <div class="hero-title" style="top:236px">To Dune Circle</div>
  <div class="btn-light">Get Started</div>
</section>

<h2 class="section-title" style="top:731px">Member Area</h2>

<div class="split-btn area-btn" style="left:111px;top:827px"><span class="label">Master Admin</span>
  <svg viewBox="0 0 40 40" fill="none" stroke="#0c3a9c" stroke-width="2"><rect x="12" y="10" width="16" height="20" rx="3"/><circle cx="20" cy="18" r="4"/><path d="M14 28c1-4 11-4 12 0M8 14h4M8 20h4M8 26h4M28 14h4M28 20h4M28 26h4"/></svg></div>
<div class="split-btn area-btn" style="left:362px;top:827px"><span class="label">Admins</span>
  <svg viewBox="0 0 40 40" fill="none" stroke="#0c3a9c" stroke-width="2"><circle cx="17" cy="13" r="6"/><path d="M5 34c0-8 6-12 12-12 3 0 5 1 7 2"/><circle cx="29" cy="29" r="5"/><circle cx="29" cy="29" r="1.5"/></svg></div>
<div class="split-btn area-btn" style="left:612px;top:827px"><span class="label">Management</span>
  <svg viewBox="0 0 40 40" fill="none" stroke="#0c3a9c" stroke-width="2"><circle cx="20" cy="20" r="13"/><circle cx="20" cy="20" r="7"/><circle cx="20" cy="18" r="2.5"/><path d="M16 25c1-3 7-3 8 0"/></svg></div>
<div class="split-btn area-btn dark" style="left:863px;top:827px"><span class="label">Marshalls</span>
  <svg viewBox="0 0 40 40" fill="none" stroke="#050a14" stroke-width="2"><circle cx="20" cy="15" r="8"/><path d="M8 36c0-8 6-12 12-12s12 4 12 12M12 15h16"/></svg></div>

<h2 class="section-title" style="top:963px">Member Level</h2>

<div class="split-btn level-btn" style="left:111px;top:1066px"><span class="label">Trail</span>
  <svg viewBox="0 0 34 34" fill="none" stroke="#0c3a9c" stroke-width="2"><rect x="4" y="13" width="26" height="10" rx="2"/><circle cx="10" cy="25" r="3.5"/><circle cx="24" cy="25" r="3.5"/><path d="M8 13l3-5h12l3 5"/></svg></div>
<div class="split-btn level-btn" style="left:310px;top:1066px"><span class="label">Mesa</span>
  <svg viewBox="0 0 34 34" fill="none" stroke="#0c3a9c" stroke-width="2"><circle cx="19" cy="8" r="3"/><path d="M19 11v9l-6 4M3 28c5-3 9-3 14 0s9 3 14 0"/></svg></div>
<div class="split-btn level-btn" style="left:508px;top:1066px"><span class="label">Falcon</span>
  <svg viewBox="0 0 34 34" fill="none" stroke="#0c3a9c" stroke-width="2"><path d="M5 22a12 12 0 0 1 24 0"/><path d="M17 22l6-8"/><path d="M9 28h16"/></svg></div>
<div class="split-btn level-btn dark" style="left:707px;top:1066px"><span class="label">Warden</span>
  <svg viewBox="0 0 34 34" fill="#050a14"><circle cx="17" cy="9" r="4"/><circle cx="8" cy="14" r="3"/><circle cx="26" cy="14" r="3"/><path d="M10 30c0-7 3-11 7-11s7 4 7 11zM2 28c0-5 2-8 6-8 2 0 3 1 3 1l-2 7zM32 28c0-5-2-8-6-8-2 0-3 1-3 1l2 7z"/></svg></div>
<div class="split-btn level-btn" style="left:905px;top:1066px"><span class="label">517</span>
  <svg viewBox="0 0 34 34" fill="none" stroke="#0c3a9c" stroke-width="2"><rect x="14" y="5" width="17" height="12"/><circle cx="8" cy="10" r="3.5"/><path d="M3 30V19c0-3 2-4 5-4l6 4M9 30v-8"/></svg></div>

<h2 class="section-title" style="top:1178px">Profile</h2>

<div class="split-btn area-btn dark" style="left:362px;top:1276px"><span class="label">Vehicle</span>
  <svg viewBox="0 0 40 40" fill="none" stroke="#050a14" stroke-width="2"><path d="M6 30l8-14h12l8 14z"/><circle cx="13" cy="32" r="3"/><circle cx="28" cy="32" r="3"/><path d="M16 16l2-6h6l2 6"/></svg></div>
<div class="split-btn area-btn" style="left:612px;top:1276px"><span class="label">Member info</span>
  <svg viewBox="0 0 40 40" fill="none" stroke="#0c3a9c" stroke-width="2"><rect x="6" y="6" width="9" height="9"/><rect x="25" y="6" width="9" height="9"/><rect x="6" y="25" width="9" height="9"/><rect x="25" y="25" width="9" height="9"/><circle cx="20" cy="20" r="4"/></svg></div>

<section class="events">
  <article class="event-card" style="left:109px">
    <div class="photo" role="img" aria-label="Photo of a grey off-road vehicle parked beside a small waterfall on rocks" style="background:linear-gradient(180deg,#e6e8ea 0%,#b9bcbf 55%,#6f6a62 100%)"></div>
    <h3>Lorem Ipsum</h3>
    <p>It is a long established fact that a reader will be distracted by the readable content of a page when looking at its layout.</p>
    <div class="meta" style="top:390px">
      <span><svg width="13" height="13" viewBox="0 0 12 12"><circle cx="6" cy="3.5" r="2.5"/><path d="M1 12c0-4 2-5 5-5s5 1 5 5z"/></svg>Contrary</span>
      <span style="margin-left:26px"><svg width="13" height="13" viewBox="0 0 12 12"><circle cx="6" cy="6" r="5.5"/><path d="M6 3v3.5h2.5" stroke="#fff" fill="none"/></svg>11:00</span>
      <span style="margin-left:26px"><svg width="11" height="14" viewBox="0 0 10 14"><path d="M5 0a5 5 0 0 0-5 5c0 4 5 9 5 9s5-5 5-9a5 5 0 0 0-5-5z"/><circle cx="5" cy="5" r="2" fill="#fff"/></svg>Mesa</span>
    </div>
    <div class="meta" style="top:420px"><span><svg width="18" height="13" viewBox="0 0 18 12"><circle cx="9" cy="3" r="2.5"/><circle cx="3.5" cy="4" r="2"/><circle cx="14.5" cy="4" r="2"/><path d="M4 12c0-4 2-6 5-6s5 2 5 6zM0 11c0-3 1-5 4-5l-1 5zM18 11c0-3-1-5-4-5l1 5z"/></svg>48 of 50</span></div>
    <div class="bar" style="top:424px"><i style="width:90%;background:var(--red)"></i></div>
  </article>

  <article class="event-card" style="left:425px">
    <div class="photo" role="img" aria-label="Photo of a dark off-road vehicle with a flag on orange desert dunes" style="background:linear-gradient(180deg,#9fc3cf 0%,#c9b08c 45%,#d88d45 100%)"></div>
    <h3>Typesetting industry</h3>
    <p>If you are going to use a passage of Lorem Ipsum, you need to be sure there isn't anything embarrassing hidden</p>
    <div class="meta" style="top:390px">
      <span><svg width="13" height="13" viewBox="0 0 12 12"><circle cx="6" cy="3.5" r="2.5"/><path d="M1 12c0-4 2-5 5-5s5 1 5 5z"/></svg>Industry</span>
      <span style="margin-left:26px"><svg width="13" height="13" viewBox="0 0 12 12"><circle cx="6" cy="6" r="5.5"/><path d="M6 3v3.5h2.5" stroke="#fff" fill="none"/></svg>10:30</span>
      <span style="margin-left:26px"><svg width="11" height="14" viewBox="0 0 10 14"><path d="M5 0a5 5 0 0 0-5 5c0 4 5 9 5 9s5-5 5-9a5 5 0 0 0-5-5z"/><circle cx="5" cy="5" r="2" fill="#fff"/></svg>Mesa</span>
    </div>
    <div class="meta" style="top:420px"><span><svg width="18" height="13" viewBox="0 0 18 12"><circle cx="9" cy="3" r="2.5"/><circle cx="3.5" cy="4" r="2"/><circle cx="14.5" cy="4" r="2"/><path d="M4 12c0-4 2-6 5-6s5 2 5 6zM0 11c0-3 1-5 4-5l-1 5zM18 11c0-3-1-5-4-5l1 5z"/></svg>10 of 30</span></div>
    <div class="bar" style="top:424px"><i style="width:55%;background:var(--blue)"></i></div>
  </article>

  <h2>Our Events</h2>
  <p class="copy">Lorem Ipsum is simply dummy text of the printing and typesetting industry. Lorem Ipsum has been the industry's standard dummy text ever since the 1500s, when an unknown printer took a galley of type and scrambled it to make a type specimen book.</p>
  <div class="split-btn" style="left:792px;top:437px;width:183px;height:57px">
    <span class="label" style="width:140px;font-size:14px">See All</span>
    <svg style="right:8px" width="40" height="16" viewBox="0 0 40 16" fill="none" stroke="#0c3a9c" stroke-width="2"><path d="M2 8h34M29 2l7 6-7 6"/></svg>
  </div>
</section>

<h2 class="section-title" style="top:2113px">About Us</h2>
<p class="about-copy">Lorem Ipsum is simply dummy text of the printing and typesetting industry. Lorem Ipsum has been the industry's standard dummy text ever since the 1500s, when an unknown printer took a galley of type and scrambled it to make a type specimen book.</p>
<div class="split-btn dark" style="left:510px;top:2303px;width:180px;height:57px">
  <span class="label" style="width:140px;font-size:18px;font-weight:500">Read More</span>
  <svg style="right:8px" width="40" height="16" viewBox="0 0 40 16" fill="none" stroke="#050a14" stroke-width="2"><path d="M2 8h34M29 2l7 6-7 6"/></svg>
</div>

<div class="photo-block" role="img" aria-label="Group photo of club members posing around an off-road vehicle in the sand" style="left:111px;top:2407px;width:978px;height:364px;border-radius:0;background:linear-gradient(180deg,#6f9fd4 0%,#a9c6e2 40%,#d9a56e 70%,#c7874d 100%)"></div>

<h2 class="section-title" style="top:2848px">Our Gallery</h2>
<svg class="arrow-nav" style="left:68px" viewBox="0 0 20 20" fill="none" stroke="#111" stroke-width="2"><path d="M13 3l-7 7 7 7"/></svg>
<div class="photo-block" role="img" aria-label="Aerial photo of a desert lake event site with vehicles spelling a word in the sand" style="left:111px;top:2932px;width:298px;height:264px;background:linear-gradient(160deg,#5b8aa0 0%,#8fb9b3 40%,#d3b58e 100%)"></div>
<div class="photo-block" role="img" aria-label="Photo of a dark grey off-road vehicle on a dune at sunset" style="left:449px;top:2932px;width:298px;height:264px;background:linear-gradient(180deg,#e7c9a3 0%,#d49a62 60%,#b87440 100%)"></div>
<div class="photo-block" role="img" aria-label="Group selfie of club members beside a vehicle" style="left:789px;top:2932px;width:298px;height:264px;background:linear-gradient(180deg,#8aa0b2 0%,#a9b4bb 50%,#6c7f8e 100%)"></div>
<svg class="arrow-nav" style="left:1110px" viewBox="0 0 20 20" fill="none" stroke="#111" stroke-width="2"><path d="M7 3l7 7-7 7"/></svg>

<h2 class="section-title" style="top:3271px">Our Blog</h2>

<article class="blog-card" style="left:111px;top:3387px;width:283px;height:482px">
  <div class="photo" role="img" aria-label="Photo of a yellow off-road vehicle climbing an orange dune" style="background:linear-gradient(180deg,#d68a45 0%,#e3a464 60%,#c77a3a 100%)"></div>
  <div class="blog-body" style="top:280px">
    <h4>Lorem Ipsum is simply<br>dummy text of the printing</h4>
    <div class="stars">★★★★★</div>
    <small>10 NoveMber 2021</small>
    <small style="margin-top:14px">4741 Hits &nbsp; 10 comments</small>
    <svg style="margin-top:12px" width="30" height="14" viewBox="0 0 30 14" fill="none" stroke="#111" stroke-width="2"><path d="M1 7h26M21 2l6 5-6 5"/></svg>
  </div>
</article>

<article class="blog-card featured" style="left:437px;top:3366px;width:321px;height:527px">
  <div class="photo" role="img" aria-label="Photo of a dark grey off-road vehicle on the dunes in warm light" style="background:linear-gradient(180deg,#dcbd95 0%,#c99866 60%,#a87446 100%)"></div>
  <div class="blog-body" style="top:301px;left:52px">
    <h4>Lorem Ipsum is simply<br>dummy text of the printing</h4>
    <div class="stars">★★★★★</div>
    <small>10 NoveMber 2021</small>
    <small style="margin-top:14px">4741 Hits &nbsp; 10 comments</small>
    <svg style="margin-top:12px" width="30" height="14" viewBox="0 0 30 14" fill="none" stroke="#111" stroke-width="2"><path d="M1 7h26M21 2l6 5-6 5"/></svg>
  </div>
</article>

<article class="blog-card" style="left:803px;top:3387px;width:283px;height:482px">
  <div class="photo" role="img" aria-label="Photo of a white off-road vehicle on rippled desert sand under a pale sky" style="background:linear-gradient(180deg,#b5c6d4 0%,#d9c2a2 50%,#c9a176 100%)"></div>
  <div class="blog-body" style="top:280px">
    <h4>Lorem Ipsum is simply<br>dummy text of the printing</h4>
    <div class="stars">★★★★★</div>
    <small>10 NoveMber 2021</small>
    <small style="margin-top:14px">4741 Hits &nbsp; 10 comments</small>
    <svg style="margin-top:12px" width="30" height="14" viewBox="0 0 30 14" fill="none" stroke="#111" stroke-width="2"><path d="M1 7h26M21 2l6 5-6 5"/></svg>
  </div>
</article>

<footer class="footer">
  <div class="pay-row" style="top:91px">
    <span class="social-dot"></span>
    <span>Orchard Pay</span>
    <span>Glide Pay</span>
  </div>
  <nav class="foot-links" style="top:218px">
    <b>Home</b><b>|</b><b>The Club</b><b>|</b><b>Community</b><b>|</b><b>Forums</b><b>|</b><b>Trips</b><b>|</b><b>Blog</b>
  </nav>
  <p class="legal" style="top:261px">Copyright © 2023 Dune Circle. All Rights Reserved.</p>
  <p class="foot-note" style="top:293px">It is a long established fact that a reader will be distracted by the readable content of a page when looking at its layout. The point of using Lorem Ipsum is that it has a more-or-less normal distribution of letters, as opposed to using 'Content here, content here', making it look like readable English.</p>
  <div class="foot-brand" style="top:149px"><span style="width:14px;height:14px;background:var(--red)"></span>Dune Circle</div>
</footer>

<div class="sponsors">
  <div class="sponsor"><i></i>WELDING</div>
  <div class="sponsor"><i></i>MECHANIC</div>
  <div class="sponsor"><i></i>WHEELS</div>
  <div class="sponsor"><i></i>TIRES</div>
  <div class="sponsor"><i></i>PAINTING</div>
</div>

</body>
</html>
```